Stationery Design Task - Stationary, memo and report templates for professional services company

Looking for someone to update stationary design but just as importantly come up with a template for reports and memos for use in our consulting firm. Would also like some brand use guidelines to be able to share with our whole team. We have an existing logo that we like. Need to update with a more contemporary look so that our deliverables to clients look good and professional yet stylish. This is for business to business communications. No need for envelope design. Important to have design for multiple pages, i.e. first page of a report and then 2nd page. Need to use in MS word documents so must be easy to use and replicate. Don't want something overly complex. Clean, fresh looking is best.

Industry/Entity Type

Information Technology

Font styles to use
Sans Serif

Colors
33a6d7
0792cd
85cae6
cee9f5
cedeed
85abd2
3377b5
0455a3

Requirements
Must have
• Clean look but with a little style or pop. Something that can easily be used in word documents. Need to have page styles that have a first page of a report (not a cover page) and then secondary page.
Nice to have
• - Although the dark blue is our primary color. Might be willing to look at some accent color as well.
Should not have
• Not just our logo on the page with a color bar.

```html
<!DOCTYPE html>
<html lang="en">
<head>
<meta charset="utf-8">
<title>Report Template Pages</title>
<link href="https://fonts.googleapis.com/css2?family=Open+Sans:wght@400;600;700&display=swap" rel="stylesheet">
<style>
:root{
  --bg:#d4d4d4;
  --ink:#1d2733;
  --blue:#0792cd;
  --blue-mid:#3377b5;
  --navy:#0455a3;
  --sky:#33a6d7;
  --pale:#cee9f5;
  --rule:#8a8a8a;
  --text:#3a3a3a;
  --paper:#ffffff;
}
*{box-sizing:border-box;margin:0;padding:0}
html,body{width:1134px;height:1200px;overflow:hidden}
body{background:var(--bg);font-family:"Open Sans",Arial,sans-serif;color:var(--text);position:relative}
.sheet-title{position:absolute;top:22px;left:0;width:100%;text-align:center;font-size:45px;font-weight:400;color:var(--ink);letter-spacing:1px}
.page{position:absolute;width:333px;height:472px;background:var(--paper);box-shadow:0 1px 4px rgba(0,0,0,.25);overflow:hidden}
.page-label{position:absolute;width:333px;text-align:center;font-size:22px;color:var(--ink)}
.p-cover{left:37px;top:106px}
.p-toc{left:398px;top:106px}
.p-intro{left:761px;top:106px}
.p-table{left:37px;top:654px}
.p-steps{left:398px;top:654px}

.header-rule{position:absolute;top:19px;left:0;width:263px;height:1px;background:var(--rule)}
.header-brand{position:absolute;top:13px;right:16px;display:flex;align-items:center;gap:3px;font-size:7.5px;font-weight:700;color:var(--navy)}
.brand-dot{width:8px;height:8px;border-radius:50%;background:var(--blue)}
.footer{position:absolute;left:15px;right:15px;top:450px;display:flex;align-items:center;gap:5px;font-size:6px;letter-spacing:1.2px;color:#333}
.footer .line{flex:1;height:1px;background:var(--blue)}
.footer .num{letter-spacing:0}
.heading{position:absolute;left:0;display:flex;align-items:center;gap:12px;font-size:10px;font-weight:700;color:var(--blue)}
.heading::before{content:"";width:3px;height:12px;background:var(--blue)}

/* cover */
.cover-art{position:absolute;left:0;top:0;width:333px;height:205px;background:linear-gradient(180deg,#ffffff 0%,#e8f4fb 100%)}
.cover-divider{position:absolute;left:20px;right:20px;top:229px;height:4px;background:linear-gradient(180deg,rgba(0,0,0,.06),rgba(0,0,0,0));border-radius:50%}
.cover-brand{position:absolute;top:258px;left:0;width:100%;display:flex;justify-content:center;align-items:center;gap:10px}
.cover-brand .mark{width:36px;height:36px;border-radius:50%;background:var(--blue)}
.cover-brand .name{font-size:24px;font-weight:700;color:var(--navy);line-height:1}
.client{position:absolute;top:362px;left:102px}
.client .name{font-size:20px;color:#111;line-height:1.2}
.client .date{font-size:15px;color:#111}
.cover-url{position:absolute;top:450px;left:0;width:100%;text-align:center;font-size:6.5px;letter-spacing:1.5px;color:#333}

/* toc */
.toc{position:absolute;top:94px;left:15px;right:15px;list-style:none}
.toc li{display:flex;align-items:center;height:20.4px;font-size:6px;color:#333}
.toc .dots{flex:1;border-bottom:1px dashed #777;margin:0 14px 0 18px;height:1px}

/* intro page */
.photo{position:absolute;left:0;width:333px}
.intro-photo{top:44px;height:144px;background:linear-gradient(120deg,#2b3a4a 0%,#9fb7cc 40%,#e9eef3 75%,#c8d3de 100%)}
.lead{position:absolute;top:230px;left:20px;right:20px;text-align:center;font-size:6.6px;font-weight:700;color:var(--navy);line-height:1.5}
.body{position:absolute;top:272px;left:15px;right:15px;font-size:5.2px;line-height:1.6;text-align:justify;color:#333}
.body p{margin-bottom:7px}

/* table page */
.subhead{position:absolute;left:15px;font-size:6.5px;font-weight:700;color:#222}
.spec{position:absolute;left:22px;width:290px;display:flex;flex-direction:column;gap:2.5px}
.spec .row{display:flex;gap:3px}
.spec .key{width:80px;background:var(--blue);color:#fff;font-size:5.5px;display:flex;align-items:center;justify-content:center}
.spec .val{flex:1;background:var(--navy);color:#fff;font-size:5.5px;padding:3px 7px;line-height:1.4;display:flex;align-items:center;text-align:justify}
.h1{min-height:17px}.h2{min-height:23px}.h3{min-height:31px}

/* steps page */
.step{position:absolute;left:16px;width:302px;height:43px;border:1.2px solid var(--navy);display:flex}
.step .badge{width:49px;background:var(--navy);display:flex;align-items:center;justify-content:center}
.step .badge span{width:17px;height:17px;border-radius:50%;border:1.5px solid #fff;background:#fff;color:var(--navy);box-shadow:0 0 0 1.5px var(--navy) inset;display:flex;align-items:center;justify-content:center;font-size:10px;font-weight:700}
.step ul{list-style:none;padding:8px 0 0 8px}
.step li{display:flex;align-items:center;gap:5px;font-size:5.3px;color:#333;height:18px}
.step li svg{width:6px;height:6px}
.steps-photo{top:278px;height:140px;background:linear-gradient(135deg,#3b2a1f 0%,#6d5140 45%,#8a6c55 70%,#4a3528 100%)}

.side-brand{position:absolute;left:788px;top:858px;display:flex;align-items:center;gap:18px}
.side-brand .mark{width:62px;height:62px;border-radius:50%;background:var(--blue)}
.side-brand .name{font-size:34px;font-weight:700;color:var(--navy);line-height:1}
</style>
</head>
<body>

<h1 class="sheet-title">WORD TEMPLATE</h1>

<!-- Cover -->
<section class="page p-cover">
  <div class="cover-art" role="img" aria-label="Decorative blue geometric cluster artwork"></div>
  <div class="cover-divider"></div>
  <div class="cover-brand"><div class="mark"></div><div class="name">LUMENCORE</div></div>
  <div class="client"><div class="name">CLIENT NAME</div><div class="date">Date, Month, Year</div></div>
  <div class="cover-url">www.lumencore-demo.com</div>
</section>
<div class="page-label" style="left:37px;top:593px">COVER PAGE</div>

<!-- Table of contents -->
<section class="page p-toc">
  <div class="header-rule"></div>
  <div class="header-brand"><span class="brand-dot"></span>LUMENCORE</div>
  <div class="heading" style="top:66px">TABLE OF CONTENTS</div>
  <ul class="toc">
    <li>Lorem Ipsum Simply Text<span class="dots"></span>03</li>
    <li>Lorem Ipsum Simply Text<span class="dots"></span>04</li>
    <li>Lorem Ipsum Simply Text<span class="dots"></span>04</li>
    <li>Lorem Ipsum Simply Text<span class="dots"></span>05</li>
    <li>Lorem Ipsum Simply Text<span class="dots"></span>06</li>
    <li>Lorem Ipsum Simply Text<span class="dots"></span>07</li>
    <li>Lorem Ipsum Simply Text<span class="dots"></span>09</li>
  </ul>
  <div class="footer"><span>www.lumencore-demo.com</span><span class="line"></span><span class="num">02</span></div>
</section>
<div class="page-label" style="left:398px;top:593px">PAGE - 02</div>

<!-- First report page -->
<section class="page p-intro">
  <div class="header-rule"></div>
  <div class="header-brand"><span class="brand-dot"></span>LUMENCORE</div>
  <div class="photo intro-photo" role="img" aria-label="Photo of hands reviewing a printed document with a pen"></div>
  <div class="heading" style="top:202px">HEADING GOES HERE</div>
  <p class="lead">Lorem Ipsum is simply dummy text of the printing and typesetting industry. Lorem Ipsum has been the industry's standard dummy text ever since the 1500s, when an unknown printer took a galley of type and scrambled it to make a type specimen book.</p>
  <div class="body">
    <p>Lorem Ipsum is simply dummy text of the printing and typesetting industry. Lorem Ipsum has been the industry's standard dummy text ever since the 1500s, when an unknown printer took a galley of type and scrambled it to make a type specimen book. It has survived not only five centuries, but also the leap into electronic typesetting, remaining essentially unchanged. It was popularised in the 1960s with the release of Transfera sheets containing Lorem Ipsum passages, and more recently with desktop publishing software like PageForge Studio including versions of Lorem Ipsum.</p>
    <p>Lorem Ipsum is simply dummy text of the printing and typesetting industry. Lorem Ipsum has been the industry's standard dummy text ever since the 1500s, when an unknown printer took a galley of type and scrambled it to make a type specimen book.</p>
    <p>Lorem Ipsum is simply dummy text of the printing and typesetting industry. Lorem Ipsum has been the industry's standard dummy text ever since the 1500s, when an unknown printer took a galley of type and scrambled it to make a type specimen book.</p>
  </div>
  <div class="footer"><span>www.lumencore-demo.com</span><span class="line"></span><span class="num">03</span></div>
</section>
<div class="page-label" style="left:761px;top:593px">PAGE - 03</div>

<!-- Table page -->
<section class="page p-table">
  <div class="header-rule"></div>
  <div class="header-brand"><span class="brand-dot"></span>LUMENCORE</div>
  <div class="heading" style="top:55px">HEADING GOES HERE</div>
  <div class="subhead" style="top:86px">LOREM IPSUM DUMMY TEXT</div>
  <div class="spec" style="top:101px">
    <div class="row h1"><div class="key">LOREM IPSUM</div><div class="val">Lorem Ipsum is simply dummy text of the printing &amp; typesetting.</div></div>
    <div class="row h2"><div class="key">LOREM IPSUM</div><div class="val">Lorem Ipsum is simply dummy text of the printing and typesetting industry.</div></div>
    <div class="row h1"><div class="key">LOREM IPSUM</div><div class="val">Lorem Ipsum is simply dummy text of the printing &amp; typesetting.</div></div>
    <div class="row h1"><div class="key">LOREM IPSUM</div><div class="val">Lorem Ipsum is simply dummy text of the printing &amp; typesetting.</div></div>
    <div class="row h2"><div class="key">LOREM IPSUM</div><div class="val">Lorem Ipsum is simply dummy text of the printing and typesetting industry.</div></div>
    <div class="row h1"><div class="key">LOREM IPSUM</div><div class="val">Lorem Ipsum is simply dummy text of the printing &amp; typesetting.</div></div>
    <div class="row h3"><div class="key">LOREM IPSUM</div><div class="val">Lorem Ipsum is simply dummy text of the printing and typesetting industry. Lorem Ipsum has been the industry's standard dummy text ever since the 1500s.</div></div>
  </div>
  <div class="subhead" style="top:276px">LOREM IPSUM DUMMY TEXT</div>
  <div class="spec" style="top:291px">
    <div class="row h1"><div class="key">LOREM IPSUM</div><div class="val">Lorem Ipsum is simply dummy text of the printing &amp; typesetting.</div></div>
    <div class="row h2"><div class="key">LOREM IPSUM</div><div class="val">Lorem Ipsum is simply dummy text of the printing and typesetting industry.</div></div>
    <div class="row h1"><div class="key">LOREM IPSUM</div><div class="val">Lorem Ipsum is simply dummy text of the printing &amp; typesetting.</div></div>
    <div class="row h1"><div class="key">LOREM IPSUM</div><div class="val">Lorem Ipsum is simply dummy text of the printing &amp; typesetting.</div></div>
    <div class="row h2"><div class="key">LOREM IPSUM</div><div class="val">Lorem Ipsum is simply dummy text of the printing and typesetting industry.</div></div>
    <div class="row h1"><div class="key">LOREM IPSUM</div><div class="val">Lorem Ipsum is simply dummy text of the printing &amp; typesetting.</div></div>
  </div>
  <div class="footer"><span>www.lumencore-demo.com</span><span class="line"></span><span class="num">04</span></div>
</section>
<div class="page-label" style="left:37px;top:1141px">PAGE - 04</div>

<!-- Steps page -->
<section class="page p-steps">
  <div class="header-rule"></div>
  <div class="header-brand"><span class="brand-dot"></span>LUMENCORE</div>
  <div class="heading" style="top:55px">HEADING GOES HERE</div>

  <div class="step" style="top:82px">
    <div class="badge"><span>1</span></div>
    <ul>
      <li><svg viewBox="0 0 10 10"><circle cx="5" cy="5" r="4.2" fill="none" stroke="#0792cd" stroke-width="1.2"/><path d="M3 5.2l1.5 1.4L7.2 3.8" fill="none" stroke="#0792cd" stroke-width="1.2"/></svg>Lorem Ipsum is simply dummy text of the printing and typesetting industry.</li>
      <li><svg viewBox="0 0 10 10"><circle cx="5" cy="5" r="4.2" fill="none" stroke="#0792cd" stroke-width="1.2"/><path d="M3 5.2l1.5 1.4L7.2 3.8" fill="none" stroke="#0792cd" stroke-width="1.2"/></svg>Lorem Ipsum is simply dummy text of the printing and typesetting industry.</li>
    </ul>
  </div>
  <div class="step" style="top:144px">
    <div class="badge"><span>2</span></div>
    <ul>
      <li><svg viewBox="0 0 10 10"><circle cx="5" cy="5" r="4.2" fill="none" stroke="#0792cd" stroke-width="1.2"/><path d="M3 5.2l1.5 1.4L7.2 3.8" fill="none" stroke="#0792cd" stroke-width="1.2"/></svg>Lorem Ipsum is simply dummy text of the printing and typesetting industry.</li>
      <li><svg viewBox="0 0 10 10"><circle cx="5" cy="5" r="4.2" fill="none" stroke="#0792cd" stroke-width="1.2"/><path d="M3 5.2l1.5 1.4L7.2 3.8" fill="none" stroke="#0792cd" stroke-width="1.2"/></svg>Lorem Ipsum is simply dummy text of the printing and typesetting industry.</li>
    </ul>
  </div>
  <div class="step" style="top:205px">
    <div class="badge"><span>3</span></div>
    <ul>
      <li><svg viewBox="0 0 10 10"><circle cx="5" cy="5" r="4.2" fill="none" stroke="#0792cd" stroke-width="1.2"/><path d="M3 5.2l1.5 1.4L7.2 3.8" fill="none" stroke="#0792cd" stroke-width="1.2"/></svg>Lorem Ipsum is simply dummy text of the printing and typesetting industry.</li>
      <li><svg viewBox="0 0 10 10"><circle cx="5" cy="5" r="4.2" fill="none" stroke="#0792cd" stroke-width="1.2"/><path d="M3 5.2l1.5 1.4L7.2 3.8" fill="none" stroke="#0792cd" stroke-width="1.2"/></svg>Lorem Ipsum is simply dummy text of the printing and typesetting industry.</li>
    </ul>
  </div>

  <div class="photo steps-photo" role="img" aria-label="Overhead photo of team fists bumping over a wooden desk with papers"></div>
  <div class="footer"><span>www.lumencore-demo.com</span><span class="line"></span><span class="num">05</span></div>
</section>
<div class="page-label" style="left:398px;top:1141px">PAGE - 05</div>

<div class="side-brand"><div class="mark"></div><div class="name">LUMENCORE</div></div>

</body>
</html>
```